Book Cover : Silent Tides: Protein Engines and the Cellular Horizon

We need a striking and engaging book cover for this new book which describes the development of the COVID-19 vaccine technology and it's potential to change the world in ways which most people don't yet realise.

On the book cover we need to include:

Silent Tides: Protein Engines and the Cellular Horizon

Safety/Efficiency/Future Applications/CRISPR

Tadeusz Głowik

Need extra days to review

```html
<!DOCTYPE html>
<html lang="en">
<head>
<meta charset="utf-8">
<title>Silent Tides: Protein Engines and the Cellular Horizon — Book Cover</title>
<link rel="stylesheet" href="https://fonts.googleapis.com/css2?family=Montserrat:wght@300;400;800&family=Nunito:wght@900&family=Lilita+One&display=swap">
<style>
  :root {
    --stage: #e6e6e6;
    --sky: #97d5e4;
    --lagoon: #2f9896;
    --ink: #0a0a0a;
    --coral: #f24638;
    --navy: #1d4f8c;
  }
  * { margin: 0; padding: 0; box-sizing: border-box; }
  html, body {
    width: 1200px;
    height: 800px;
    overflow: hidden;
    background: var(--stage);
  }
  .canvas {
    position: relative;
    width: 1200px;
    height: 800px;
  }
  .cover {
    position: absolute;
    left: 367px;
    top: 40px;
    width: 466px;
    height: 720px;
    background: var(--sky);
    overflow: hidden;
  }
  .cover-art {
    position: absolute;
    left: 0;
    top: 0;
    width: 466px;
    height: 720px;
  }
  .line {
    position: absolute;
    left: 0;
    width: 100%;
    text-align: center;
    line-height: 1;
    white-space: nowrap;
  }
  .title-strong {
    font-family: "Nunito", sans-serif;
    font-weight: 900;
    color: var(--ink);
  }
  .title-accent {
    font-family: "Lilita One", sans-serif;
    color: var(--coral);
    letter-spacing: 1px;
  }
  .title-light {
    font-family: "Montserrat", sans-serif;
    font-weight: 300;
    color: var(--ink);
  }
  .title-1 { top: 188px; font-size: 54px; padding-left: 30px; }
  .title-2 { top: 252px; font-size: 60px; }
  .title-3 { top: 331px; font-size: 42px; }
  .title-4 { top: 401px; font-size: 40px; }
  .title-5 { top: 465px; font-size: 44px; }
  .topics {
    font-family: "Montserrat", sans-serif;
    font-weight: 400;
    color: var(--ink);
    font-size: 18px;
    letter-spacing: 2px;
  }
  .topics-1 { top: 562px; }
  .topics-2 { top: 587px; }
  .author {
    top: 655px;
    font-family: "Montserrat", sans-serif;
    font-weight: 400;
    font-size: 36px;
    letter-spacing: 4px;
    color: var(--navy);
  }
</style>
</head>
<body>
<main class="canvas">
  <section class="cover">
    <svg class="cover-art" viewBox="0 0 466 720" role="img" aria-label="Illustration: paper-cut teal waves with a globe, floating virus particles and a syringe">
      <path d="M0 0 H180 C150 60 212 100 200 160 C190 220 252 250 240 300 L228 342 L0 507 Z" fill="var(--lagoon)"/>
    </svg>

    <h1 class="book-title">
      <span class="line title-strong title-1">Silent</span>
      <span class="line title-accent title-2">Tides:</span>
      <span class="line title-strong title-3">Protein Engines</span>
      <span class="line title-light title-4">and the Cellular</span>
      <span class="line title-light title-5">Horizon</span>
    </h1>

    <p class="line topics topics-1">Safety/Efficiency</p>
    <p class="line topics topics-2">Future Applications/CRISPR</p>

    <p class="line author">Tadeusz Głowik</p>
  </section>
</main>
</body>
</html>
```